Electrical Contractor's Business Stationary

I need a custom designed Stationery set for my Electrical Contracting business.

My trading business name is "BLUEMARSH ELECTRICAL" please use this name and the attached vektor file of my trademarked logo

I have a (Pixel Harbor) designed logo & font style I have trademarked, and would like that used in the Stationary.

I need to be able to write to clients with letterhead's and footers, so my business can display that we are a professional team.

Please stick with the colours of "Green/Red/Black" as in my logo, on white backgrounds

Target Market(s)

Commercial clients/customers

Residential clients/customers

Industrial clients/customers

Home owners

Business owners

Holiday home owners

Investors

First home buyers

Industry/Entity Type

Business

Requirements
Must have
• Must be in A4 format

My trademarked logo (file uploaded & can you add a very small "TM" at the end)

my TWPL group membership logo (which I have also included)

My Electrical Contractor License No,
My ABN (Australian Business Number),
My email address,
My Website address,

my mobile phone - fax - office phone numbers
(As per screenshot of a sample invoice which is attached, and these details can be strung out along the bottom footer or wherever, as I'm looking for inventiveness )

And the areas my business covers " SYDNEY - CENTRAL COAST - NEWCASTLE", somewhere on the stationary also.

Thanks guys!!

```html
<!DOCTYPE html>
<html lang="en">
<head>
<meta charset="utf-8">
<title>Bluemarsh Electrical – Business Cards</title>
<link rel="stylesheet" href="https://fonts.googleapis.com/css2?family=Open+Sans:wght@400;700&display=swap">
<style>
  :root {
    --page-bg: #e9e7e3;
    --card-bg: #f4f4f4;
    --brand-red: #c8202b;
    --brand-green: #7fb82a;
    --band-grey: #8a8a8a;
    --ink: #2b2b2b;
    --ink-soft: #555555;
    --white: #ffffff;
  }
  * { box-sizing: border-box; margin: 0; padding: 0; }
  html, body {
    width: 1200px; height: 900px; overflow: hidden;
    background: var(--page-bg);
    font-family: "Open Sans", Arial, sans-serif;
  }
  .stationery {
    position: relative; width: 1200px; height: 900px;
  }
  .card {
    position: absolute; width: 520px; height: 318px;
    background: var(--card-bg);
    box-shadow: 0 2px 10px rgba(0,0,0,0.12);
    overflow: hidden;
  }
  .card--back { left: 45px; top: 291px; }
  .card--front { left: 635px; top: 291px; }

  /* Back of card */
  .licence-band {
    position: absolute; left: 0; right: 0; top: 14px; height: 18px;
    background: var(--band-grey);
    color: var(--white); font-size: 10px; line-height: 18px;
    padding-left: 22px; letter-spacing: 0.3px;
  }
  .wordmark {
    display: flex; align-items: center; gap: 14px;
  }
  .wordmark__dot {
    width: 34px; height: 34px; border-radius: 50%;
    background: var(--brand-green); flex: none;
  }
  .wordmark__name {
    color: var(--brand-red); font-weight: 700;
    font-size: 30px; line-height: 1; letter-spacing: 0.5px;
  }
  .wordmark__tm { font-size: 10px; vertical-align: top; }
  .card--back .wordmark {
    position: absolute; left: 0; right: 0; top: 118px; justify-content: center;
  }
  .areas-band {
    position: absolute; left: 0; right: 0; bottom: 26px; height: 26px;
    background: var(--brand-red);
    color: var(--white); font-size: 12px; line-height: 26px;
    text-align: center; letter-spacing: 0.6px;
  }

  /* Front of card */
  .card--front .wordmark { position: absolute; left: 34px; top: 66px; }
  .card--front .wordmark__name { font-size: 27px; }
  .website {
    position: absolute; left: 34px; top: 106px;
    font-size: 12px; color: var(--ink-soft);
  }
  .website strong { color: var(--brand-red); font-weight: 700; }
  .person {
    position: absolute; left: 34px; top: 178px;
    display: flex; align-items: baseline; gap: 8px;
  }
  .person__name { font-size: 19px; color: var(--ink); letter-spacing: 0.4px; }
  .person__role { font-size: 11px; color: var(--ink); }
  .contacts {
    position: absolute; left: 34px; top: 216px;
    display: flex; gap: 16px;
    font-size: 12.5px; color: var(--ink); line-height: 20px;
  }
  .contacts__group { padding-right: 16px; }
  .contacts__group + .contacts__group { border-left: 1px solid #9a9a9a; padding-left: 14px; padding-right: 0; }
  .contacts__label { color: var(--brand-red); display: inline-block; width: 16px; }
</style>
</head>
<body>
<main class="stationery">

  <section class="card card--back" aria-label="Business card back">
    <div class="licence-band">Electrical Contractor License No. 118205c</div>
    <div class="wordmark">
      <span class="wordmark__dot"></span>
      <span class="wordmark__name">BLUEMARSH ELECTRICAL<span class="wordmark__tm">TM</span></span>
    </div>
    <div class="areas-band">SYDNEY - CENTRAL COAST - NEWCASTLE</div>
  </section>

  <section class="card card--front" aria-label="Business card front">
    <div class="wordmark">
      <span class="wordmark__name">BLUEMARSH ELECTRICAL<span class="wordmark__tm">TM</span></span>
    </div>
    <p class="website">www.<strong>bluemarshelectrical</strong>.com.au</p>
    <div class="person">
      <span class="person__name">MARA LINDQVIST</span>
      <span class="person__role">Principal designer</span>
    </div>
    <div class="contacts">
      <div class="contacts__group">
        <div><span class="contacts__label">T</span>(02) 4187 2260</div>
        <div><span class="contacts__label">M</span>0400 615 928</div>
      </div>
      <div class="contacts__group">
        <div><span class="contacts__label">F</span>(02) 4187 2261</div>
        <div><span class="contacts__label">E</span>accounts@bluemarshelectrical.com.au</div>
      </div>
    </div>
  </section>

</main>
</body>
</html>
```